Larkspur Vision Optometrists

News paper advertisement (150mm H x 110mm W).
Eye testing (Salubra covered).
Prescription glasses,sunglasses & contact lenses.
All major health funds accepted.
Phone: 95550132 for an appointment at our Claremont practice
or Phone: 95550478 for an appointment at our Subiaco practice.
Please disregard "Good health for less" slogan.
We are an independent Optometry practice providing major fashion brands in both Optical frames & sunglasses.
Keep it simple and / or entertaining.
Use of company logo not critical, only discretionary.
Use as much or as little of this information as you wish.

```html
<!DOCTYPE html>
<html lang="en">
<head>
<meta charset="utf-8">
<title>Larkspur Vision Optometrists – Eye Testing</title>
<link rel="stylesheet" href="https://fonts.googleapis.com/css2?family=Jost:wght@400&family=Arimo:wght@400;700&display=swap">
<style>
  :root {
    --page: #e6feff;
    --hands: #a6f4fb;
    --band: #00c8f8;
    --blue: #1a34d6;
    --ink: #2b2b2b;
    --red: #f00a0a;
    --white: #ffffff;
  }
  * { margin: 0; padding: 0; box-sizing: border-box; }
  html, body { width: 900px; height: 1200px; overflow: hidden; }
  body { background: var(--page); font-family: "Arimo", Arial, sans-serif; }

  .ad { position: relative; width: 900px; height: 1200px; background: var(--page); overflow: hidden; }

  .headline { position: absolute; top: 52px; left: 0; width: 100%; text-align: center; }
  .headline__title { font-family: "Jost", "Futura", sans-serif; font-weight: 400; font-size: 46px; line-height: 1; color: var(--blue); letter-spacing: 1px; }
  .headline__cover { font-weight: 700; font-size: 20px; color: var(--blue); margin-top: 2px; }
  .headline__services { font-size: 24px; color: var(--ink); margin-top: 6px; }

  .hero { position: absolute; top: 160px; left: 0; width: 900px; height: 540px; }

  .funds { position: absolute; top: 724px; left: 0; width: 100%; text-align: center; }
  .funds__text { display: inline-block; color: var(--red); font-size: 22px; padding: 6px 8px; border-top: 1px dotted var(--red); border-bottom: 1px dotted var(--red); }

  .contacts { position: absolute; top: 784px; left: 0; width: 100%; text-align: center; font-size: 21px; line-height: 32px; }
  .contacts__phone { color: var(--blue); }
  .contacts__practice { color: var(--red); font-weight: 700; }

  .footer-band { position: absolute; left: 0; bottom: 0; width: 900px; height: 138px; background: var(--band); }
  .footer-band__text { position: absolute; top: 62px; width: 100%; text-align: center; color: var(--white); font-size: 23px; line-height: 32px; }

  .brand { position: absolute; top: 930px; left: 325px; width: 250px; height: 178px; background: var(--white); border-radius: 8px; display: flex; align-items: center; justify-content: center; gap: 12px; }
  .brand__mark { width: 22px; height: 22px; background: var(--blue); }
  .brand__name { font-family: "Arimo", Arial, sans-serif; font-weight: 700; font-size: 26px; line-height: 1.15; color: var(--blue); text-align: left; }
</style>
</head>
<body>
<main class="ad">
  <header class="headline">
    <h1 class="headline__title">EYE TESTING</h1>
    <p class="headline__cover">(SALUBRA COVERED)</p>
    <p class="headline__services">Prescription glasses, sunglasses &amp; contact lenses.</p>
  </header>

  <svg class="hero" viewBox="0 0 900 540" aria-hidden="false">
    <defs>
      <linearGradient id="photoTone" x1="0" y1="0" x2="1" y2="0">
        <stop offset="0" stop-color="#e8b9a0"/>
        <stop offset="0.5" stop-color="#d9a58c"/>
        <stop offset="0.75" stop-color="#c9d2e0"/>
        <stop offset="1" stop-color="#2a4fd8"/>
      </linearGradient>
    </defs>
    <g role="img" aria-label="Two open hands drawn in light aqua, cupped around the eye-shaped photograph">
      <path class="hero__hands" d="M0 60 C200 40 420 20 620 30 C760 40 840 10 900 0 L900 390 C760 420 620 470 470 500 C300 530 120 530 0 500 Z" fill="var(--hands)"/>
    </g>
    <path role="img" aria-label="Photograph of a young woman having her eyes examined at an optometry instrument"
          d="M159 265 C300 100 580 100 720 265 C580 440 300 440 159 265 Z" fill="url(#photoTone)"/>
  </svg>

  <div class="funds"><p class="funds__text">ALL MAJOR HEALTH FUNDS ACCEPTED.</p></div>

  <section class="contacts">
    <p class="contacts__phone">Phone: 95550132 for an appointment at our</p>
    <p class="contacts__practice">CLAREMONT PRACTICE</p>
    <p class="contacts__phone">Phone: 95550478 for an appointment at our</p>
    <p class="contacts__practice">SUBIACO PRACTICE.</p>
  </section>

  <footer class="footer-band">
    <p class="footer-band__text">We are an independent Optometry practice providing major<br>fashion brands in both Optical frames &amp; sunglasses.</p>
  </footer>

  <div class="brand">
    <span class="brand__mark"></span>
    <span class="brand__name">Larkspur<br>Vision</span>
  </div>
</main>
</body>
</html>
```